VELMORA BRIDGE ADVISORY

Need a Boucher designed with vibrant colours and well aligned. The content is there in the word file what I have attached. The heading and the subject of each paragraph has to be separated by designing accordingly. I would appreciate if nice hd pictures of stock market/trading/forex/consulting can be accommodated with this.

Target Market(s)

traders, stock traders, business entrepreneurs

Font styles to use
Sans Serif

Requirements
Must have
• Images from stock market and charts
Nice to have
• I want it to look elegant as this goes to the trading community.
Should not have
• Don't want anything that looks goody or fashionable since its a professional broucher.

```html
<!DOCTYPE html>
<html lang="en">
<head>
<meta charset="utf-8">
<title>Trading A Serious Business — Velmora Bridge Advisory Brochure</title>
<link href="https://fonts.googleapis.com/css2?family=Oswald:wght@500;600&family=Lato:ital,wght@0,400;0,700;0,900;1,400&display=swap" rel="stylesheet">
<style>
  :root {
    --stage: #5b4130;
    --paper: #ffffff;
    --blue-deep: #0b3f8c;
    --blue-mid: #1565c0;
    --blue-bright: #2a8be0;
    --blue-sky: #4aa6ee;
    --orange: #f6a01a;
    --ink: #2d2d2d;
    --ink-soft: #5a5a5a;
    --logo-grey: #4a4a4a;
    --steel: #9aa3ab;
  }
  * { box-sizing: border-box; margin: 0; padding: 0; }
  html, body { width: 1200px; height: 907px; overflow: hidden; }
  body { background: var(--stage); font-family: "Lato", sans-serif; position: relative; }

  .page {
    position: absolute; top: 98px; width: 500px; height: 647px;
    background: var(--paper); overflow: hidden;
    box-shadow: 0 6px 18px rgba(0,0,0,.35);
  }
  .page--cover { left: 66px; }
  .page--inside { left: 622px; width: 501px; }

  /* ---------- Cover ---------- */
  .cover-art { position: absolute; inset: 0; width: 500px; height: 647px; }
  .brand {
    position: absolute; top: 356px; left: 0; width: 500px;
    display: flex; justify-content: center; align-items: center; gap: 12px;
  }
  .brand__mark { width: 44px; height: 44px; background: var(--blue-mid); }
  .brand__name {
    font-family: "Lato", sans-serif; font-weight: 900; font-size: 30px;
    letter-spacing: 1px; color: var(--logo-grey);
  }
  .cover-title {
    position: absolute; top: 458px; left: 0; width: 500px; text-align: center;
    font-family: "Oswald", sans-serif; font-weight: 600; font-size: 27px;
    color: #fff; letter-spacing: .2px;
  }
  .cover-rule {
    position: absolute; top: 502px; left: 60px; width: 380px; height: 1px;
    background: linear-gradient(90deg, transparent, rgba(255,255,255,.55), transparent);
  }
  .cover-subtitle {
    position: absolute; top: 506px; left: 0; width: 500px; text-align: center;
    font-size: 18px; line-height: 23px; color: #fff;
  }
  .cover-byline {
    position: absolute; top: 578px; right: 52px; text-align: right;
    font-style: italic; font-size: 11px; line-height: 13px; color: #fff;
    text-transform: uppercase;
  }

  /* ---------- Inside ---------- */
  .inside-art { position: absolute; inset: 0; width: 501px; height: 647px; }
  .section-title {
    position: absolute; top: 34px; left: 20px;
    font-family: "Lato", sans-serif; font-weight: 900; font-size: 21px;
    color: #fff; letter-spacing: .3px;
  }
  .body-copy {
    position: absolute; top: 101px; left: 20px; width: 457px;
    font-size: 8.4px; line-height: 10.6px; color: var(--ink); text-align: justify;
  }
  .key-points {
    position: absolute; top: 331px; left: 38px; width: 439px; list-style: none;
  }
  .key-point {
    position: relative; padding-left: 13px; margin-bottom: 9px;
    font-size: 8.4px; line-height: 10.6px; color: var(--ink); text-align: justify;
  }
  .key-point__tick { position: absolute; left: 0; top: 1px; width: 10px; height: 9px; }
  .key-point__head { color: var(--blue-mid); font-weight: 900; }
</style>
</head>
<body>

<!-- Front page -->
<section class="page page--cover">
  <svg class="cover-art" viewBox="0 0 500 647" aria-hidden="false">
    <defs>
      <linearGradient id="photoTone" x1="0" y1="0" x2="0" y2="1">
        <stop offset="0" stop-color="#1d5fd6"/>
        <stop offset=".6" stop-color="#0d3fa6"/>
        <stop offset="1" stop-color="#082a74"/>
      </linearGradient>
      <linearGradient id="coverPanel" x1="0" y1="0" x2="0" y2="1">
        <stop offset="0" stop-color="#1e7fdc"/>
        <stop offset="1" stop-color="#1359b8"/>
      </linearGradient>
    </defs>
    <!-- white base -->
    <rect width="500" height="647" fill="#fff"/>
    <!-- orange band -->
    <path d="M0,262 C140,318 330,322 500,262 V292 C330,344 140,340 0,300 Z" fill="var(--orange)"/>
    <!-- blue band -->
    <path d="M0,250 C140,304 330,306 500,244 V270 C330,326 140,324 0,274 Z" fill="var(--blue-mid)"/>
    <!-- photo area -->
    <path d="M0,0 H500 V232 C330,292 140,290 0,240 Z" fill="url(#photoTone)"
          role="img" aria-label="Photo of business people in suits standing before a glowing world map"/>
    <!-- bottom blue panel -->
    <rect x="0" y="432" width="500" height="215" fill="url(#coverPanel)"/>
    <!-- orange foot band -->
    <path d="M0,636 V634 Q0,624 14,624 H486 Q500,624 500,634 V647 H0 Z" fill="var(--orange)"/>
  </svg>

  <div class="brand">
    <span class="brand__mark"></span>
    <span class="brand__name">VELMORA</span>
  </div>

  <h1 class="cover-title">“TRADING” A SERIOUS BUSINESS,</h1>
  <div class="cover-rule"></div>
  <p class="cover-subtitle">Importance of Capital and The Rise in<br>Proprietary Trading Firm</p>
  <p class="cover-byline">By<br>Velmora Bridge Advisory<br>Taren Malvik</p>
</section>

<!-- Page 1 -->
<section class="page page--inside">
  <svg class="inside-art" viewBox="0 0 501 647">
    <defs>
      <linearGradient id="ribbon" x1="0" y1="0" x2="0" y2="1">
        <stop offset="0" stop-color="#1a6ec9"/>
        <stop offset="1" stop-color="#0b4a9a"/>
      </linearGradient>
      <linearGradient id="techTone" x1="0" y1="0" x2="1" y2="0">
        <stop offset="0" stop-color="#0c2a4a"/>
        <stop offset=".6" stop-color="#123f66"/>
        <stop offset="1" stop-color="#0a2238"/>
      </linearGradient>
    </defs>
    <!-- title ribbon -->
    <path d="M0,27 H435 L460,70 H0 Z" fill="url(#ribbon)"/>
    <path d="M0,73 H300 L250,76 H0 Z" fill="var(--steel)" opacity=".6"/>
    <!-- bottom bands -->
    <path d="M0,520 C150,470 350,470 501,512 V530 C350,492 150,492 0,540 Z" fill="var(--orange)"/>
    <path d="M0,530 C150,482 350,482 501,522 V540 C350,500 150,500 0,550 Z" fill="var(--blue-mid)"/>
    <path d="M0,545 C150,496 350,496 501,536 V647 H0 Z" fill="url(#techTone)"
          role="img" aria-label="Photo of a hand touching glowing digital interface icons in front of server racks"/>
  </svg>

  <h2 class="section-title">TRADING IS A SERIOUS BUSINESS</h2>

  <div class="body-copy">
    <p>One of the biggest mistakes amateur traders make is that they don’t treat their trading like a business</p>
    <p>When we often interact with aspiring traders, and one question they always ask me is this: “How long it takes to be successful in this business?” Now that’s an interesting question, mainly because the trading profession appears to be deceptively simple.</p>
    <p>Let me explain in a bit more detail. Let’s take any business and presume you want to venture into that. What all things you need to start the business and make it a successful venture? You would look at your area of competence, the product, regulatory approvals, the competitors, pricing, advertising &amp; marketing, sales, logistics and so on &amp; so forth. It would take many months or even years, depending on the type of business (which is called gestation period) to attain breakeven and make profit. Compare this business example with trading. What do we need to become a successful trader? Virtually nothing! Open an account with a broker and you will become a trader!! It is the simplicity of the process that makes the trading business so deceptive. A trader doesn’t require any license to start trading, nor does he need to have any prior qualification, or do any kind of marketing, sales, etc. Consequently, all those who feel this process is very simple end up being disappointed because trading is easy to start, but is highly challenging to make into a full-time profession. It’s a process to be precise.</p>
    <p>One of the biggest mistakes amateur traders make is: They don’t treat their trading like a business. Instead, they treat it like a trip to a casino and many of them end up becoming gambling addicts instead of calm &amp;rational traders. If you treat trading like any other business, your attitude towards it would change and the results will eventually follow. Remember, it’s not a ‘get rich quick’ scheme! So, what are the factors you need to consider before you get into trading?</p>
  </div>

  <ul class="key-points">
    <li class="key-point">
      <svg class="key-point__tick" viewBox="0 0 10 9"><path d="M1,5 L4,8 L9,1" fill="none" stroke="var(--orange)" stroke-width="2"/></svg>
      <span class="key-point__head">HAVE A TRADING PLAN</span> - Just like a business plan one must have a proper plan for trading. It can be a very exhaustive plan. It should outline the asset classes you wish to trade in, the strategy to employ for each of them, the capital you wish to deploy, the amount of money you wish to risk or make - per week/per month/per year, the tools you will use, rules you will follow, etc. Everything should be clearly written in black &amp; white.
    </li>
    <li class="key-point">
      <svg class="key-point__tick" viewBox="0 0 10 9"><path d="M1,5 L4,8 L9,1" fill="none" stroke="var(--orange)" stroke-width="2"/></svg>
      <span class="key-point__head">UNDERGO THE PROCESS</span> – To become a trader, its important to develop all the skills that are required to be a pro trader. The Psychology and mindset of the trader plays a very important role in becoming successful in this business. Believe in the process.
    </li>
    <li class="key-point">
      <svg class="key-point__tick" viewBox="0 0 10 9"><path d="M1,5 L4,8 L9,1" fill="none" stroke="var(--orange)" stroke-width="2"/></svg>
      <span class="key-point__head">STRATEGY &amp; RISK MANAGEMENT</span> – All you need is a strategy with a proven track record, backed by solid risk management principles. The only way to excel in any profession is to learn from someone who is already doing what you intend to do. Approach someone who can teach you the key trading skills.
    </li>
  </ul>
</section>

</body>
</html>
```